Aquarium Folder

Design for 12" x 9" folder

OVERALL LOOK

Colorful but classy looking, catered mainly to potential customers looking to book weddings, corporate events, etc.

COLORS/FONTS

Century Gothic for small copy, Any larger headlines (if you choose to use) should be in Headline, Triplex Serif, or Marcelle Script

FRONT COVER

LMH Logo (includes)
Picture of shark exhibit (in Filecrate folder)

LEFT INSIDE COVER

Pictures of exhibits/event space found here: https://www.filecrate.example/sh/q7w2kd9ra4vx1mz/BQRtLpW8xZc3NvYhe58KjTqdPs?dl=0

Should feature at minumum – Shark exhibit, Underwater event space, Dolphins, Fish, Sloth, Otter

Copy:

Welcome to the Lone Mesa Marine Hall, where you’re invited to Wander a Wider Realm on an awe-inspiring adventure through land and sea. Travel through the lush jungles and vibrant coral reefs of the Yucatan Peninsula in Tropic Voyage, where you’ll encounter flamingos, sharks, free-flying birds, reptiles, and even a sloth. Dive deeper into the underwater world in the Gulf of Mexico, where you’ll come face-to-face with sharks, stingrays, eagles and hundreds of other species. You’ll experience dive shows, animal feedings, training sessions, and hands-on programs with sharks, stingrays, and even jellies, and take in the amazing behaviors of dolphins, otters, birds, and more during our daily wildlife presentations. Catch a show in the immersive Brisketbarn 4-Dimension Theater and during the warmer months, cool off in a kid-friendly water playground

The Lone Mesa Marine Hall welcomes more than half a million guests each year who come to soak in the sights at our exhibits, presentations, or other attractions or commemorate a special event in our after-hours venues. The Tropic Voyage includes an expansive naturally-lit jungle where birds fly freely throughout, bright flamingos lounge in a lagoon, and aquatic overlooks hint at the underwater world waiting below. In Tropic Voyage’s underwater level, you’ll step into the immersive habitats of the colorful Pearl Shelf and the mysterious Deep Well, and venture into the 400,000 P-L-Q Tropic Sea. This gigantic depiction of an underwater Caribbean reef features a life-size shipwreck, the longest display window in North America, and a underwater tunnel, where guests can behold sharks, stingrays, groupers, and other species from just inches away. The Gulf of Mexico contains dozens of additional exhibits, including Towers of Iron, depicting the life that teems under offshore oil platforms, Petal Meadows, showcasing a real-Pearl Shelf that lies off the Texas coast, and Armreach, with the otherworldly octopus and jellies. Get up close and personal with dolphins from above and below the water in Porpoise Cove, and look to the skies as hawks, owl, and falcon soar above in the Brell Sky Wing Theater. Touch and hand-feed stingrays at Skate Pool, enjoy the energetic antics of otters in Mink Brook, watch as sea turtles gracefully glide In the waters of Galapa Key, and spy on an alligator and other scaly reptiles in the Marsh Yarns. The fun continues in the Brisketbarn 4-Dimension Theater, which screens 3D films with interactive special effects, and the P-L-Q Splash Park, a zero-depth water playscape (open in spring and summer).

Looking for an unforgettable venue for your special event? After-hours event spaces are available in our most stunning aquatic exhibits including the P-L-Q Tropic Sea, Towers of Iron, and the Caribbean jungle look to give your get-together a truly unique backdrop with boundless photo opportunities. In the upstairs PETRAX Horizon Venue, 300 guests can be seated in an elegant dining room overlooking the sparkling Palomar Harborfront. These events can include our in-house catering, a dedicated event planner, animal encounters, dive shows, and other highlights to make the most of your event.

Open since 1990 and accredited by the Guild of Menageries and Marine Parks, the Lone Mesa Marine Hall is a nonprofit institution with the mission is to engage people with animals, inspire appreciation for our seas, and support wildlife conservation. When you visit our facility, purchase from our gift shop or restaurants, or celebrate in one of our private event spaces, you’re helping us make a difference for the environment and the community. This includes the care of our animals and the upkeep of our exhibits, which bring to life the stories of marine and coastal animals and teach why it’s so important to conserve these species and their habitats. Your support of the Lone Mesa Marine Hall also helps fund our Creature Aid and Return program, which treats hundreds of injured, ill, or stranded shorebirds, raptors, sea turtles, and marine mammals each year and works to release them back into their natural habitat.

What’s more, the Lone Mesa Marine Hall teaches more than 70,000 children each year through its environmental education programs featuring STEM Learning activities as part of the Oakridge Fuels Hub for Mastery in STEM (science, technology, engineering, math) Education. These programs, provide both on-site and through outreach and distance learning initiatives, are creating the next generation of scientists, educators, and environmental leaders.

Every visit to the Lone Mesa Marine Hall is a new and exciting discovery that remind us all of our responsibility to the animals we share our world with. With so much to see and experience, you’re sure to enjoy a day with your family full of fun, discovery, and learning, so what are you waiting for? Visit us today or reserve your event today and Wander a Wider Realm.

INSIDE FIRST PAGE

Cutout for business card
LMH Logo

```html
<!DOCTYPE html>
<html lang="en">
<head>
<meta charset="utf-8">
<title>Lone Mesa Marine Hall — Event Folder</title>
<link rel="stylesheet" href="https://fonts.googleapis.com/css2?family=Questrial&display=swap">
<style>
  :root {
    --stage: #dfe6ee;
    --ocean-deep: #1f4f9a;
    --ocean-mid: #2f74c6;
    --ocean-light: #5fa3e3;
    --ocean-pale: #a9cdf1;
    --reef-warm: #c98a3a;
    --paper: #f1f2f4;
    --paper-shade: #e1e3e7;
    --ink: #5b5f66;
    --white: #ffffff;
    --logo-blue: #1f5fae;
    --ring: #3b82d6;
  }
  * { box-sizing: border-box; margin: 0; padding: 0; }
  html, body { width: 1005px; height: 1200px; overflow: hidden; }
  body {
    background: var(--stage);
    font-family: "Questrial", "Century Gothic", sans-serif;
    position: relative;
  }
  .spread {
    position: absolute;
    left: 67px;
    width: 870px;
    height: 580px;
    display: flex;
    box-shadow: 0 4px 14px rgba(20, 50, 100, 0.22);
  }
  .spread--outside { top: 13px; }
  .spread--inside { top: 607px; }
  .panel { position: relative; width: 435px; height: 580px; overflow: hidden; }

  /* Back cover */
  .back-cover { background: linear-gradient(180deg, #3d86d2 0%, #2d6cbf 55%, #2a5fa8 100%); }
  .back-cover__photo {
    position: absolute; left: 40px; top: 150px; width: 360px; height: 430px;
    background: radial-gradient(ellipse at 55% 40%, rgba(150,170,190,0.55), rgba(90,120,160,0.25) 55%, rgba(0,0,0,0) 75%);
  }
  .back-cover__reef {
    position: absolute; left: 0; bottom: 0; width: 100%; height: 150px;
    background: linear-gradient(180deg, rgba(60,120,190,0) 0%, rgba(70,110,160,0.5) 100%);
  }
  .back-cover__copy {
    position: absolute; left: 52px; top: 56px; width: 330px;
    color: var(--white); font-size: 13px; line-height: 1.42; text-align: center;
  }
  .back-cover__web {
    position: absolute; left: 0; width: 100%; bottom: 62px;
    color: var(--white); font-size: 15px; text-align: center; letter-spacing: 0.2px;
  }
  .back-cover__web strong { font-weight: 400; font-size: 17px; }

  /* Front cover */
  .front-cover {
    background: linear-gradient(180deg, #6aa9e6 0%, #2e7fd0 30%, #1d5fb3 55%, #3e86c9 70%, #6d8fa8 100%);
  }
  .front-cover__photo { position: absolute; inset: 0; }
  .front-cover__reef {
    position: absolute; left: 0; bottom: 0; width: 100%; height: 210px;
    background: linear-gradient(180deg, rgba(201,138,58,0) 0%, rgba(201,138,58,0.55) 45%, rgba(170,110,70,0.75) 100%);
  }
  .brand {
    position: absolute; top: 58px; right: 38px;
    display: flex; align-items: center; gap: 8px;
    color: var(--logo-blue); font-size: 20px; line-height: 1;
  }
  .brand__dot { width: 22px; height: 22px; border-radius: 50%; background: var(--reef-warm); }

  /* Inside left */
  .inside-left { background: var(--paper); }
  .inside-left svg.wave { position: absolute; inset: 0; }
  .photo-circle {
    position: absolute; border-radius: 50%;
    border: 5px solid var(--ring); box-shadow: 0 0 0 3px var(--white);
  }
  .photo-circle--venue { left: 132px; top: 40px; width: 116px; height: 116px; background: radial-gradient(circle at 50% 45%, #5d88b5, #2b4a70); }
  .photo-circle--otter { left: 272px; top: 90px; width: 116px; height: 116px; background: radial-gradient(circle at 50% 45%, #8c6a4e, #4f3d2e); }
  .photo-circle--sloth { left: 48px; top: 150px; width: 116px; height: 116px; background: radial-gradient(circle at 50% 45%, #a17a58, #5e6a45); }
  .photo-circle--dolphin { left: 300px; top: 240px; width: 116px; height: 116px; background: radial-gradient(circle at 50% 45%, #9cc3dd, #3d7fb4); }
  .photo-circle--shark { left: 60px; top: 330px; width: 116px; height: 116px; background: radial-gradient(circle at 50% 45%, #4d8ac3, #1b3f6e); }
  .photo-circle--fish { left: 220px; top: 375px; width: 116px; height: 116px; background: radial-gradient(circle at 50% 45%, #8f7ac9, #c9a43e); }

  /* Inside right */
  .inside-right { background: linear-gradient(90deg, var(--paper-shade) 0%, var(--paper) 12%); }
  .inside-right svg.wave { position: absolute; inset: 0; }
  .body-copy {
    position: absolute; left: 42px; top: 40px; width: 360px;
    color: var(--ink); font-size: 6.1px; line-height: 1.36;
  }
  .body-copy p { margin-bottom: 6px; }
</style>
</head>
<body>

<section class="spread spread--outside">
  <div class="panel back-cover">
    <div class="back-cover__photo" role="img" aria-label="Faded photo of an otter with a shark swimming behind"></div>
    <div class="back-cover__reef" role="img" aria-label="Faded coral reef"></div>
    <p class="back-cover__copy">Every visit to the Lone Mesa Marine Hall is a new and exciting discovery that remind us all of our responsibility to the animals we share our world with. With so much to see and experience, you’re sure to enjoy a day with your family full of fun, discovery, and learning, so what are you waiting for? Visit us today or reserve your event today and Wander a Wider Realm.</p>
    <p class="back-cover__web">www.<strong>LoneMesaMarineHall</strong>.org</p>
  </div>
  <div class="panel front-cover">
    <div class="front-cover__photo" role="img" aria-label="Photo of the shark exhibit with sharks and fish over a coral reef"></div>
    <div class="front-cover__reef"></div>
    <div class="brand"><span class="brand__dot"></span><span>Lone Mesa Marine Hall</span></div>
  </div>
</section>

<section class="spread spread--inside">
  <div class="panel inside-left">
    <svg class="wave" width="435" height="580" viewBox="0 0 435 580">
      <defs>
        <linearGradient id="leftSea" x1="0" y1="0" x2="0" y2="1">
          <stop offset="0" stop-color="#4b95df"/>
          <stop offset="1" stop-color="#2c68b8"/>
        </linearGradient>
      </defs>
      <path d="M0 232 C 60 300, 150 250, 230 190 C 300 140, 370 120, 435 130 L435 580 L0 580 Z" fill="#a9cdf1"/>
      <path d="M0 246 C 60 310, 150 262, 232 202 C 300 154, 370 136, 435 144 L435 580 L0 580 Z" fill="url(#leftSea)"/>
      <rect x="0" y="330" width="435" height="250" fill="#3a6fae" opacity="0.35" role="img" aria-label="Faded coral reef with fish"/>
    </svg>
    <div class="photo-circle photo-circle--venue" role="img" aria-label="Photo of the underwater event space set for dinner"></div>
    <div class="photo-circle photo-circle--otter" role="img" aria-label="Photo of an otter"></div>
    <div class="photo-circle photo-circle--sloth" role="img" aria-label="Photo of a sloth"></div>
    <div class="photo-circle photo-circle--dolphin" role="img" aria-label="Photo of two dolphins"></div>
    <div class="photo-circle photo-circle--shark" role="img" aria-label="Photo of a shark in the exhibit"></div>
    <div class="photo-circle photo-circle--fish" role="img" aria-label="Photo of a tropical angelfish"></div>
  </div>

  <div class="panel inside-right">
    <svg class="wave" width="435" height="580" viewBox="0 0 435 580">
      <defs>
        <linearGradient id="rightSea" x1="0" y1="0" x2="1" y2="0">
          <stop offset="0" stop-color="#5aa0e2"/>
          <stop offset="1" stop-color="#2f74c6"/>
        </linearGradient>
      </defs>
      <path d="M0 470 C 90 500, 200 505, 300 480 C 360 465, 410 440, 435 420 L435 580 L0 580 Z" fill="#a9cdf1"/>
      <path d="M0 488 C 90 520, 200 522, 300 498 C 360 484, 410 462, 435 444 L435 580 L0 580 Z" fill="url(#rightSea)"/>
      <rect x="300" y="470" width="135" height="110" fill="#9fb6cc" opacity="0.55" role="img" aria-label="Photo of two dolphins"/>
    </svg>
    <div class="body-copy">
      <p>Welcome to the Lone Mesa Marine Hall, where you’re invited to Wander a Wider Realm on an awe-inspiring adventure through land and sea. Travel through the lush jungles and vibrant coral reefs of the Yucatan Peninsula in Tropic Voyage, where you’ll encounter flamingos, sharks, free-flying birds, reptiles, and even a sloth. Dive deeper into the underwater world in the Gulf of Mexico, where you’ll come face-to-face with sharks, stingrays, eagles and hundreds of other species. You’ll experience dive shows, animal feedings, training sessions, and hands-on programs with sharks, stingrays, and even jellies, and take in the amazing behaviors of dolphins, otters, birds, and more during our daily wildlife presentations. Catch a show in the immersive Brisketbarn 4-Dimension Theater and during the warmer months, cool off in a kid-friendly water playground.</p>
      <p>The Lone Mesa Marine Hall welcomes more than half a million guests each year who come to soak in the sights at our exhibits, presentations, or other attractions or commemorate a special event in our after-hours venues. The Tropic Voyage includes an expansive naturally-lit jungle where birds fly freely throughout, bright flamingos lounge in a lagoon, and aquatic overlooks hint at the underwater world waiting below. In Tropic Voyage’s underwater level, you’ll step into the immersive habitats of the colorful Pearl Shelf and the mysterious Deep Well, and venture into the 400,000 P-L-Q Tropic Sea. This gigantic depiction of an underwater Caribbean reef features a life-size shipwreck, the longest display window in North America, and a underwater tunnel, where guests can behold sharks, stingrays, groupers, and other species from just inches away. The Gulf of Mexico contains dozens of additional exhibits, including Towers of Iron, depicting the life that teems under offshore oil platforms, Petal Meadows, showcasing a real Pearl Shelf that lies off the Texas coast, and Armreach, with the otherworldly octopus and jellies. Get up close and personal with dolphins from above and below the water in Porpoise Cove, and look to the skies as hawks, owl, and falcon soar above in the Brell Sky Wing Theater. Touch and hand-feed stingrays at Skate Pool, enjoy the energetic antics of otters in Mink Brook, watch as sea turtles gracefully glide in the waters of Galapa Key, and spy on an alligator and other scaly reptiles in the Marsh Yarns. The fun continues in the Brisketbarn 4-Dimension Theater, which screens 3D films with interactive special effects, and the P-L-Q Splash Park, a zero-depth water playscape (open in spring and summer).</p>
      <p>Looking for an unforgettable venue for your special event? After-hours event spaces are available in our most stunning aquatic exhibits including the P-L-Q Tropic Sea, Towers of Iron, and the Caribbean jungle look to give your get-together a truly unique backdrop with boundless photo opportunities. In the upstairs PETRAX Horizon Venue, 300 guests can be seated in an elegant dining room overlooking the sparkling Palomar Harborfront. These events can include our in-house catering, a dedicated event planner, animal encounters, dive shows, and other highlights to make the most of your event.</p>
      <p>Open since 1990 and accredited by the Guild of Menageries and Marine Parks, the Lone Mesa Marine Hall is a nonprofit institution with the mission is to engage people with animals, inspire appreciation for our seas, and support wildlife conservation. When you visit our facility, purchase from our gift shop or restaurants, or celebrate in one of our private event spaces, you’re helping us make a difference for the environment and the community. This includes the care of our animals and the upkeep of our exhibits, which bring to life the stories of marine and coastal animals and teach why it’s so important to conserve these species and their habitats. Your support of the Lone Mesa Marine Hall also helps fund our Creature Aid and Return program, which treats hundreds of injured, ill, or stranded shorebirds, raptors, sea turtles, and marine mammals each year and works to release them back into their natural habitat.</p>
      <p>What’s more, the Lone Mesa Marine Hall teaches more than 70,000 children each year through its environmental education programs featuring STEM Learning activities as part of the Oakridge Fuels Hub for Mastery in STEM (science, technology, engineering, math) Education. These programs, provide both on-site and through outreach and distance learning initiatives, are creating the next generation of scientists, educators, and environmental leaders.</p>
    </div>
  </div>
</section>

</body>
</html>
```